Banner Ad Design Project

We need a 728x90 and a 300x250
1st option
"I have a lead for you. Click here to close the deal."
In large bold letters.
Under this in smaller letters,
"Borwelt. For serious business networkers"
2nd option
"Put that coffee down!"
"Coffee's for closers only."
Close more deals. BORWELT LOGO
(this is a quote from Harrowmere Tavish. It is a famous sales movie)
The other option is
"First you get the money" "Then you get the power" in bold letters.
"Borwelt. For serious business networkers" in smaller letters at the bottom.
-Must have our colors
-Must have our logo (Small at the bottom right)
-Watch the video at borwelt () com
Please be creative. If the banner can have multiple images that would be great as well.
This needs to be a serious looking ad that is bold and clean.
Updates
Please be sure to use the phrase, "Put that coffee down! Coffee's for closers only" with the logo and at the bottom the words, Borwelt, for serious business networkers. in one of the designs. This will be our first campaign. I am looking for a very simple design that is bold. Perhaps just a coffee cup with the words and no other graphics.
Target Market(s)
Sales professionals
Industry/Entity Type
Business
Look and feel

```html
<!DOCTYPE html>
<html lang="en">
<head>
<meta charset="utf-8">
<title>Borwelt banner set</title>
<link rel="stylesheet" href="https://fonts.googleapis.com/css2?family=Arimo:wght@400;700&display=swap">
<style>
  :root {
    --backdrop: #333333;
    --banner-top: #2b65b3;
    --banner-bottom: #1d3d78;
    --paper: #ffffff;
    --headline: #ffffff;
    --photo-warm: #d8cfc7;
    --photo-light: #f4f1ee;
    --brand-ink: #3c5f9e;
    --brand-square: #f0961e;
  }
  * { margin: 0; padding: 0; box-sizing: border-box; }
  html, body {
    width: 1200px;
    height: 600px;
    overflow: hidden;
    background: var(--backdrop);
  }
  .canvas {
    position: relative;
    width: 1200px;
    height: 600px;
    background: var(--backdrop);
    font-family: "Arimo", Arial, sans-serif;
  }
  .banner {
    position: absolute;
    left: 163px;
    width: 874px;
    height: 108px;
    overflow: hidden;
    background: linear-gradient(to bottom, var(--banner-top), var(--banner-bottom));
  }
  .banner--headline { top: 120px; }
  .banner--closers { top: 247px; }
  .banner--tagline { top: 374px; }

  .banner__paper {
    position: absolute;
    left: 0;
    top: 0;
    width: 260px;
    height: 108px;
  }
  .banner__paper path { fill: var(--paper); }

  .photo-slot {
    position: absolute;
    top: 0;
    height: 108px;
    background: linear-gradient(135deg, var(--photo-warm), var(--photo-light));
  }
  .banner--headline .photo-slot { left: 30px; width: 124px; }
  .banner--closers .photo-slot { left: 0; width: 58px; }

  .banner__text {
    position: absolute;
    color: var(--headline);
    font-weight: 700;
    white-space: nowrap;
    text-shadow: 0 1px 2px rgba(0, 0, 0, 0.25);
  }
  .banner--headline .banner__text { left: 284px; top: 27px; font-size: 44px; letter-spacing: 4.4px; }
  .banner--closers .banner__text { left: 139px; top: 27px; font-size: 44px; letter-spacing: 3.9px; }
  .banner--tagline .banner__text { left: 271px; top: 35px; font-size: 29px; letter-spacing: 4.2px; }

  .brand-card {
    position: absolute;
    left: 18px;
    top: 12px;
    width: 233px;
    height: 84px;
    background: var(--paper);
    transform: rotate(-2deg);
    box-shadow: 0 2px 5px rgba(0, 0, 0, 0.35);
    display: flex;
    align-items: center;
    justify-content: center;
    gap: 12px;
  }
  .brand-card__mark {
    width: 30px;
    height: 30px;
    background: var(--brand-square);
  }
  .brand-card__name {
    font-size: 30px;
    font-weight: 400;
    color: var(--brand-ink);
  }
</style>
</head>
<body>
<main class="canvas">
  <section class="banner banner--headline">
    <svg class="banner__paper" viewBox="0 0 260 108" aria-hidden="true">
      <path d="M0,0 H155 Q218,32 228,108 H0 Z"/>
    </svg>
    <div class="photo-slot" role="img" aria-label="Photo of a cup of black coffee on a saucer, seen from above"></div>
    <p class="banner__text">Put that coffee down!</p>
  </section>

  <section class="banner banner--closers">
    <svg class="banner__paper" viewBox="0 0 260 108" aria-hidden="true">
      <path d="M0,0 H86 Q112,30 121,108 H0 Z"/>
    </svg>
    <div class="photo-slot" role="img" aria-label="Photo of the edge of a coffee cup on a saucer"></div>
    <p class="banner__text">Coffee's for closers only</p>
  </section>

  <section class="banner banner--tagline">
    <div class="brand-card">
      <span class="brand-card__mark" aria-hidden="true"></span>
      <span class="brand-card__name">Borwelt</span>
    </div>
    <p class="banner__text">For serious business networkers</p>
  </section>
</main>
</body>
</html>
```